Healthy Snack Bar Wrapper Design

We are passionate about delivering healthy and tasty treats that are Raw, Organic, Preservative Free, Gluten Free, have No Added Sugar and No Additives!
In this project we are looking for a design for a new healthy food product to be launched soon in Australia. The packaging will be a bar wrapper made from foil that will be hot sealed, with a front and a back.
The snack is a raw, organic and healthy treat made predominantly with nuts, and will come in 3 initial flavours:
- Velvet Harbor (Sour Cherry and Choc)
- Plum Fizzaroo (Banana, Apricot and Blueberry)
- Sunmelodia (Pineapple, Passionfruit and Kiwi)
The product name is MunchWell, which does not currently have a logo. We are happy to have this as a simple written component of the initial design at the top of the packaging, perhaps within an circle, square or oval.
The typeface used for the names and the main ingredients should be fun.
The overall design should be very simple and make use of minimal colours. Our preferences are to have a plain colour for the background, such as light organic brown or white, with an eye catching colour that can be used to define the flavour, but should not be too vibrant.
We do not want to have an 3 dimensional images or objects. Nor do we want to have product images and any imagery should be only to give the impression of the flavours within rather than an image of the flavour. Finally, we do not want to have gradients included in the design.
The final design should communicate healthy, tasty and fun!
Examples of inspiration designs are attached in the files.
Main Information:
- The front should comprise of the following information:
-- MunchWell
-- Flavour name (such as Velvet Harbor)
-- Main Ingredients (Sour Cherry and Choc) (This is optional)
-- Portion size (60g)
-- Message (This is optional)
--- 0% Additives
--- 60% Nuts
--- 100% Natural
- The back needs to have space for the following information:
-- Nutritional Information
-- Barcode
-- Ingredients
-- Contact information
- Wrapper Dimensions
-- Width: 14cm
-- Height: 15cm
- Bar Dimensions
-- Width: 3cm
-- Height: 10cm
-- Depth: 2.5cm
Target Market(s)
People who want to have a healthy tasty treat
Colors
Designer to choose colors to be used in the design.
Requirements
Must have
- Main Information:
- - The front should comprise of the following information:
- -- MunchWell
- -- Flavour name (such as Velvet Harbor)
- -- Main Ingredients (Sour Cherry and Choc) (This is optional)
- -- Portion size (60g)
- -- Message (This is optional)
- --- 0% Additives
- --- 60% Nuts
- --- 100% Natural
- - The back needs to have space for the following information:
- -- Nutritional Information
- -- Barcode
- -- Ingredients
- -- Contact information
- - Wrapper Dimensions
- -- Width: 14cm
- -- Height: 15cm
- - Bar Dimensions
- -- Width: 3cm
- -- Height: 10cm
- -- Depth: 2.5cm
Should not have
- We do not want to have an 3 dimensional images or objects. Nor do we want to have product images and any imagery should be only to give the impression of the flavours within rather than an image of the flavour. Finally, we do not want to have gradients included in the design.

```html
<!DOCTYPE html>
<html lang="en">
<head>
<meta charset="UTF-8">
<title>MunchWell Snack Bar Wrappers</title>
<link href="https://fonts.googleapis.com/css2?family=Amatic+SC:wght@700&family=Quicksand:wght@600;700&display=swap" rel="stylesheet">
<style>
  :root {
    --bg: #dcdbdb;
    --dark: #2e2e30;
    --white: #ffffff;
    --plum: #c96fae;
    --orange: #e8a043;
    --lime: #c2d42e;
  }
  * { margin: 0; padding: 0; box-sizing: border-box; }
  html, body { width: 1200px; height: 1200px; overflow: hidden; }
  body { background: var(--bg); position: relative; font-family: "Quicksand", sans-serif; }
  .defs { position: absolute; width: 0; height: 0; }

  .wrapper {
    position: absolute; top: 280px; width: 280px;
    display: flex; flex-direction: column;
  }
  .wrapper--plum { left: 90px; --flavour: var(--plum); }
  .wrapper--orange { left: 460px; --flavour: var(--orange); }
  .wrapper--lime { left: 830px; --flavour: var(--lime); }

  .crimp { display: block; width: 280px; height: 12px; }
  .seal-top { height: 100px; background: var(--flavour); position: relative; }
  .brand {
    position: absolute; left: 50%; bottom: -55px; transform: translateX(-50%);
    width: 116px; height: 116px; border-radius: 50%;
    background: var(--dark); color: var(--white);
    display: flex; align-items: center; justify-content: center;
    font-weight: 700; font-size: 19px; z-index: 2;
  }
  .panel {
    background: var(--dark); padding: 74px 20px 22px; text-align: center;
  }
  .flavour-name {
    font-family: "Amatic SC", cursive; font-weight: 700;
    color: var(--white); font-size: 66px; line-height: 0.92; letter-spacing: 1px;
  }
  .flavour-name--long { font-size: 60px; }
  .ingredients {
    margin-top: 14px; color: var(--flavour);
    font-weight: 700; font-size: 22px; line-height: 1.1;
  }
  .claims { background: var(--flavour); list-style: none; }
  .claims li {
    height: 30px; border-bottom: 3px solid var(--dark);
    display: flex; align-items: center; justify-content: center;
    color: var(--dark); font-weight: 600; font-size: 14px; gap: 5px;
  }
  .claims li:first-child { border-top: 3px solid var(--dark); }
  .claims li:last-child { border-bottom: none; }
  .claims strong { font-size: 19px; font-weight: 700; }
  .seal-bottom {
    height: 96px; background: var(--dark); color: var(--white);
    display: flex; align-items: center; justify-content: center;
    font-weight: 700; font-size: 26px;
  }
</style>
</head>
<body>
<svg class="defs" aria-hidden="true">
  <defs>
    <pattern id="teeth-up-plum" width="10" height="12" patternUnits="userSpaceOnUse"><path d="M0 12 L5 0 L10 12 Z" fill="#c96fae"/></pattern>
    <pattern id="teeth-up-orange" width="10" height="12" patternUnits="userSpaceOnUse"><path d="M0 12 L5 0 L10 12 Z" fill="#e8a043"/></pattern>
    <pattern id="teeth-up-lime" width="10" height="12" patternUnits="userSpaceOnUse"><path d="M0 12 L5 0 L10 12 Z" fill="#c2d42e"/></pattern>
    <pattern id="teeth-down-dark" width="10" height="12" patternUnits="userSpaceOnUse"><path d="M0 0 L5 12 L10 0 Z" fill="#2e2e30"/></pattern>
  </defs>
</svg>

<article class="wrapper wrapper--plum">
  <svg class="crimp" viewBox="0 0 280 12"><rect width="280" height="12" fill="url(#teeth-up-plum)"/></svg>
  <div class="seal-top"><div class="brand">MunchWell</div></div>
  <div class="panel">
    <h2 class="flavour-name">PLUM<br>FIZZAROO</h2>
    <p class="ingredients">banana, apricot<br>&amp; blueberry</p>
  </div>
  <ul class="claims">
    <li><strong>0%</strong> additives</li>
    <li><strong>60%</strong> nuts</li>
    <li><strong>100%</strong> natural</li>
  </ul>
  <div class="seal-bottom">60g</div>
  <svg class="crimp" viewBox="0 0 280 12"><rect width="280" height="12" fill="url(#teeth-down-dark)"/></svg>
</article>

<article class="wrapper wrapper--orange">
  <svg class="crimp" viewBox="0 0 280 12"><rect width="280" height="12" fill="url(#teeth-up-orange)"/></svg>
  <div class="seal-top"><div class="brand">MunchWell</div></div>
  <div class="panel">
    <h2 class="flavour-name">VELVET<br>HARBOR</h2>
    <p class="ingredients">Sour Cherry<br>&amp; Choc</p>
  </div>
  <ul class="claims">
    <li><strong>0%</strong> additives</li>
    <li><strong>60%</strong> nuts</li>
    <li><strong>100%</strong> natural</li>
  </ul>
  <div class="seal-bottom">60g</div>
  <svg class="crimp" viewBox="0 0 280 12"><rect width="280" height="12" fill="url(#teeth-down-dark)"/></svg>
</article>

<article class="wrapper wrapper--lime">
  <svg class="crimp" viewBox="0 0 280 12"><rect width="280" height="12" fill="url(#teeth-up-lime)"/></svg>
  <div class="seal-top"><div class="brand">MunchWell</div></div>
  <div class="panel">
    <h2 class="flavour-name flavour-name--long">SUN<br>MELODIA</h2>
    <p class="ingredients">pineapple, kiwi<br>&amp; passionfruit</p>
  </div>
  <ul class="claims">
    <li><strong>0%</strong> additives</li>
    <li><strong>60%</strong> nuts</li>
    <li><strong>100%</strong> natural</li>
  </ul>
  <div class="seal-bottom">60g</div>
  <svg class="crimp" viewBox="0 0 280 12"><rect width="280" height="12" fill="url(#teeth-down-dark)"/></svg>
</article>
</body>
</html>
```